Torvel, Inc. new buisness cards - brand guide included

We need new business cards. SLEAK SIMPLE FINANCE. They must include a place for NAME, TITLE, CELL, OFFICE PHONE, EMAIL. they also must include our services across the bottom. AIR, OCEAN, FTL, LTL, EXPRESS. for reference this will be being handed to some of the most prestigious shipping companies in a america.

Target Market(s)

Finance and corporate

Contact Information for Business Card

We need new business cards. SLEAK SIMPLE FINANCE. They must include a place for NAME, TITLE, CELL, OFFICE PHONE, EMAIL. they also must include our services across the bottom. AIR, OCEAN, FTL, LTL, EXPRESS.

Requirements
Must have
• We need new business cards. SLEAK SIMPLE FINANCE. They must include a place for NAME, TITLE, CELL, OFFICE PHONE, EMAIL. they also must include our services across the bottom. AIR, OCEAN, FTL, LTL, EXPRESS.
Nice to have
• USE THE COLORS AND LOGO IN THE BRAND GUIDE :)

```html
<!DOCTYPE html>
<html lang="en">
<head>
<meta charset="utf-8">
<title>Torvel, Inc. — Business Cards</title>
<link href="https://fonts.googleapis.com/css2?family=Montserrat:wght@400;500;600&family=Arimo:wght@400&display=swap" rel="stylesheet">
<style>
  :root {
    --backdrop: #767676;
    --card-white: #fcfcfd;
    --gold: #b6a47f;
    --gold-fill: #c3b393;
    --gold-line: #cbbd9f;
    --ink: #222222;
    --muted: #9a9a9a;
    --white: #ffffff;
  }
  * { margin: 0; padding: 0; box-sizing: border-box; }
  html, body {
    width: 1200px; height: 802px; overflow: hidden;
    background: var(--backdrop);
  }
  .stage {
    position: relative; width: 1200px; height: 802px;
    display: flex; align-items: center; justify-content: center; gap: 40px;
  }
  .card {
    position: relative; width: 540px; height: 310px;
    border-radius: 18px; overflow: hidden;
  }
  .card--front { background: var(--card-white); }
  .card--back {
    background: var(--gold-fill);
    display: flex; align-items: center; justify-content: center;
  }
  .brand-name {
    font-family: "Montserrat", sans-serif; font-weight: 500;
    letter-spacing: 6px; text-transform: uppercase;
  }
  .card--front .brand-name {
    position: absolute; left: 42px; top: 112px;
    font-size: 34px; color: var(--gold);
  }
  .card--back .brand-name { font-size: 58px; color: var(--white); letter-spacing: 10px; }
  .identity { position: absolute; left: 262px; top: 34px; }
  .identity__name {
    font-family: "Montserrat", sans-serif; font-weight: 600;
    font-size: 25px; letter-spacing: 1px; color: var(--gold); text-transform: uppercase;
  }
  .identity__title {
    font-family: "Arimo", sans-serif; font-size: 14px; color: var(--muted); margin-top: 2px;
  }
  .contacts { list-style: none; margin-top: 14px; }
  .contacts li {
    display: flex; align-items: center; gap: 10px; height: 23px;
    font-family: "Arimo", sans-serif; font-size: 14px; color: var(--ink);
  }
  .contacts svg { width: 13px; height: 13px; flex: none; }
  .divider {
    position: absolute; left: 52px; right: 44px; top: 236px;
    height: 1px; background: var(--gold-line);
  }
  .services-tag {
    position: absolute; left: 50%; top: 236px; transform: translate(-50%, -50%);
    padding: 4px 20px; border: 1px solid var(--gold-line); border-radius: 14px;
    background: var(--card-white);
    font-family: "Arimo", sans-serif; font-size: 13px; letter-spacing: 1px; color: var(--gold);
  }
  .services-list {
    position: absolute; left: 0; right: 0; top: 262px; text-align: center;
    font-family: "Arimo", sans-serif; font-size: 16px; letter-spacing: 0.5px; color: var(--ink);
  }
  .services-list .dot { color: var(--gold); margin: 0 6px; }
</style>
</head>
<body>
<main class="stage">
  <section class="card card--front" aria-label="Business card front">
    <div class="brand-name">Torvel</div>
    <div class="identity">
      <h1 class="identity__name">Selin Arvas</h1>
      <p class="identity__title">Founder &amp; CEO</p>
      <ul class="contacts">
        <li>
          <svg viewBox="0 0 16 16" fill="var(--gold)"><path d="M3.6 1.5l2.3 2.6-1.3 1.8c.9 2 2.5 3.6 4.5 4.5l1.8-1.3 2.6 2.3-1.2 2.4C7.2 13.6 2.4 8.8 1.2 3z"/></svg>
          015-372-604-118
        </li>
        <li>
          <svg viewBox="0 0 16 16" fill="var(--gold)"><path d="M1 5.5C2.5 3.5 5 2.5 8 2.5s5.5 1 7 3l-2 1.6-2-1.2V4.6H5v1.3L3 7.1z"/><path d="M4 8h8l1.5 6h-11z"/><circle cx="8" cy="11" r="1.6" fill="var(--card-white)"/></svg>
          048-216-390-547
        </li>
        <li>
          <svg viewBox="0 0 16 16" fill="var(--gold)"><path d="M15 1L1 7l5 2 2 5z"/></svg>
          hello@torvelmail.com
        </li>
        <li>
          <svg viewBox="0 0 16 16" fill="none" stroke="var(--gold)" stroke-width="1.6"><circle cx="8" cy="8" r="6.5"/><path d="M1.5 8h13M8 1.5c-3 3.5-3 9.5 0 13M8 1.5c3 3.5 3 9.5 0 13"/></svg>
          www.torvelfreight.com
        </li>
      </ul>
    </div>
    <div class="divider"></div>
    <div class="services-tag">SERVICES</div>
    <p class="services-list">AIR<span class="dot">•</span>OCEAN<span class="dot">•</span>FTL<span class="dot">•</span>LTL<span class="dot">•</span>EXPRESS</p>
  </section>

  <section class="card card--back" aria-label="Business card back">
    <div class="brand-name">Torvel</div>
  </section>
</main>
</body>
</html>
```